New Outdoor Fitness Flyer Project

Hi, we need a flyer design in A5 side (one sided preferably) for a new company based in Singapore called "Tide Motion". We are an outdoor based fitness company who offer personal training for 1 on 1 clients, kickboxing, HIIT (high intensity interval training), group classes out door based training. Catering for all fitness levels & age groups. Please view our website www.tidemotion-sg.example for more details.

As we are new to the industry, we need the flyer as our major advertising for now so the needs to pop and catch peoples attention.

Our logos are uploaded for usage for design of flyer.

Target Market(s)

We would love to target anyone with any fitness level.

Industry/Entity Type

Advertising

Requirements
Must have
• -types of trainings we offer (such as 1 on 1 Personal Training, Buddy Training, Kick boxing & Outdoor Group classes)

-we cater to all fitness level and age group.

-Anytime, Anywhere, At Your Own Convenience.

-Tagline (please choose one which is more suitable for the design): "Archive Faster Weight Loss & Muscle Gain", "Better Lifestyle Starts With Healthy Workout" or "Be Fit.Be Strong."

-our contact details:
M: 8164-5290
E: daniel@tidemotion-sg.example
W: www.tidemotion-sg.example

-call us now for a free trial! terms & conditions apply
Nice to have
• Please include pictures not given on our website as we would like to have something different.

```html
<!DOCTYPE html>
<html lang="en">
<head>
<meta charset="utf-8">
<title>Tide Motion – Outdoor Fitness Flyer</title>
<link rel="stylesheet" href="https://fonts.googleapis.com/css2?family=Ubuntu:ital,wght@0,400;0,500;0,700;1,400;1,700&display=swap">
<style>
  :root {
    --ink-deep: #14212a;
    --ink-mid: #22343f;
    --ink-soft: #2d4350;
    --blue: #1aa6e8;
    --blue-bright: #3cc3f5;
    --blue-dark: #0b5f9c;
    --silver: #c9d0d5;
    --silver-dark: #7d878e;
    --white: #ffffff;
    --text: #e9eef1;
    --muted: #cdd5da;
    --logo: #e85aa8;
    --studio-light: #e3ecf3;
    --studio-glass: #b9cddd;
    --studio-skin: #d9aa98;
    --studio-pink: #d77ba3;
    --studio-floor: #8e9bb4;
    --studio-mat: #2a63b5;
    --photo-kick-a: #f0e6dc;
    --photo-kick-b: #c08464;
    --photo-pt-a: #f1ebe8;
    --photo-pt-b: #b0645c;
  }
  * { margin: 0; padding: 0; box-sizing: border-box; }
  html, body { width: 927px; height: 1200px; overflow: hidden; background: var(--ink-deep); }
  .flyer {
    position: relative; width: 927px; height: 1200px; overflow: hidden;
    font-family: "Ubuntu", sans-serif; color: var(--text);
    background: radial-gradient(ellipse at 55% 75%, var(--ink-soft) 0%, var(--ink-mid) 45%, var(--ink-deep) 100%);
  }
  .artwork { position: absolute; inset: 0; }
  .brand {
    position: absolute; left: 30px; top: 76px; width: 285px; height: 44px;
    background: linear-gradient(180deg, #9aa3a9, #4c555b);
    clip-path: polygon(0 0, 100% 0, 92% 100%, 0 100%);
    display: flex; align-items: center; padding-left: 14px;
  }
  .brand-name { font-weight: 700; font-size: 27px; color: var(--logo); letter-spacing: 0.5px; }
  .headline {
    position: absolute; left: 46px; top: 408px;
    font-weight: 700; font-size: 53px; line-height: 1.08; color: var(--white);
    text-shadow: 0 2px 8px rgba(0,0,0,0.55), 0 0 2px rgba(0,0,0,0.4);
  }
  .intro { position: absolute; left: 66px; top: 756px; font-size: 17px; line-height: 29px; }
  .services { list-style: none; }
  .services li { position: relative; padding-left: 18px; }
  .services li::before {
    content: ""; position: absolute; left: 1px; top: 9px;
    border-left: 11px solid transparent; border-bottom: 11px solid var(--blue);
  }
  .audience { margin-top: 5px; }
  .slogan {
    position: absolute; left: 66px; top: 950px;
    font-style: italic; font-weight: 700; font-size: 19px; color: var(--blue);
  }
  .cta { position: absolute; left: 64px; top: 994px; font-weight: 700; font-size: 30px; color: var(--white); }
  .contact { position: absolute; left: 66px; top: 1048px; list-style: none; }
  .contact li { display: flex; align-items: center; gap: 9px; font-weight: 500; font-size: 16px; color: var(--white); height: 25px; }
  .contact .phone { font-weight: 700; font-size: 29px; color: var(--blue); height: 38px; }
  .contact svg { flex: none; }
  .terms { position: absolute; left: 66px; top: 1156px; font-size: 16px; color: var(--muted); }
  .caption {
    position: absolute; right: 64px; font-style: italic; font-size: 13px; color: var(--muted);
    display: flex; align-items: center; gap: 10px;
  }
  .caption::after { content: ""; border-left: 10px solid transparent; border-bottom: 10px solid var(--blue); }
  .caption-kick { top: 901px; }
  .caption-pt { top: 1120px; }
</style>
</head>
<body>
<main class="flyer">
  <svg class="artwork" width="927" height="1200" viewBox="0 0 927 1200">
    <defs>
      <linearGradient id="heroTone" x1="0" y1="0" x2="0.15" y2="1">
        <stop offset="0" stop-color="var(--studio-light)"/>
        <stop offset="0.3" stop-color="var(--studio-glass)"/>
        <stop offset="0.55" stop-color="var(--studio-skin)"/>
        <stop offset="0.68" stop-color="var(--studio-pink)"/>
        <stop offset="0.82" stop-color="var(--studio-floor)"/>
        <stop offset="1" stop-color="var(--studio-mat)"/>
      </linearGradient>
      <linearGradient id="kickTone" x1="0" y1="0" x2="1" y2="1">
        <stop offset="0" stop-color="var(--photo-kick-a)"/>
        <stop offset="1" stop-color="var(--photo-kick-b)"/>
      </linearGradient>
      <linearGradient id="ptTone" x1="0" y1="0" x2="1" y2="1">
        <stop offset="0" stop-color="var(--photo-pt-a)"/>
        <stop offset="1" stop-color="var(--photo-pt-b)"/>
      </linearGradient>
      <linearGradient id="swooshBlue" x1="0" y1="0" x2="1" y2="0">
        <stop offset="0" stop-color="var(--blue-dark)"/>
        <stop offset="0.5" stop-color="var(--blue)"/>
        <stop offset="1" stop-color="var(--blue-bright)"/>
      </linearGradient>
      <linearGradient id="swooshSilver" x1="0" y1="0" x2="1" y2="0">
        <stop offset="0" stop-color="var(--silver-dark)"/>
        <stop offset="0.5" stop-color="var(--silver)"/>
        <stop offset="1" stop-color="var(--silver-dark)"/>
      </linearGradient>
    </defs>

    <path class="hero-silver" fill="url(#swooshSilver)"
      d="M0 600 C70 630 150 648 235 655 L300 718 L340 690 L700 668 C840 625 915 470 927 330 L927 300 C900 470 820 600 700 640 L330 668 L300 700 L230 640 C140 630 60 610 0 590 Z"/>
    <path class="hero-blue" fill="url(#swooshBlue)"
      d="M0 540 C90 585 200 605 300 598 L690 575 C830 530 905 390 927 220 L927 300 C900 470 820 600 700 640 L330 668 L300 700 L230 640 C140 630 60 610 0 590 Z"/>
    <path class="hero-photo" role="img" aria-label="Photo: group of smiling women stretching on blue mats in a bright fitness studio"
      fill="url(#heroTone)"
      d="M0 0 H927 V220 C905 390 830 530 690 575 L300 598 C200 605 90 585 0 540 Z"/>

    <path role="img" aria-label="Photo: woman in boxing gloves at a punching bag" fill="url(#kickTone)"
      d="M690 718 H927 V880 H615 Z"/>
    <path class="photo-bar" fill="url(#swooshBlue)" d="M615 878 H927 V891 H622 Z"/>

    <path role="img" aria-label="Photo: trainer guiding a woman lifting a barbell" fill="url(#ptTone)"
      d="M690 935 H927 V1097 H615 Z"/>
    <path class="photo-bar" fill="url(#swooshBlue)" d="M615 1095 H927 V1108 H622 Z"/>

    <path fill="url(#swooshSilver)" d="M385 1122 C520 1132 640 1150 720 1200 H560 C520 1170 460 1145 385 1122 Z"/>
    <path fill="url(#swooshBlue)" d="M410 1150 C520 1160 610 1175 650 1200 H470 C450 1180 430 1165 410 1150 Z"/>
  </svg>

  <div class="brand"><span class="brand-name">Tide Motion</span></div>

  <h1 class="headline">Better Lifestyle Starts<br>With Healthy Workout</h1>

  <section class="intro">
    <p>We are an outdoor based fitness company who offer:</p>
    <ul class="services">
      <li>Personal Training for 1 on 1 clients</li>
      <li>Kick Boxing</li>
      <li>HIIT (High Intensity Interval Training)</li>
      <li>Group Classes out door based training.</li>
    </ul>
    <p class="audience">We cater to all fitness level and age group.</p>
  </section>

  <p class="slogan">Anytime, Anywhere, At Your Own Convenience.</p>
  <p class="cta">CALL US NOW FOR A FREE TRIAL!</p>

  <ul class="contact">
    <li class="phone">
      <svg width="14" height="16" viewBox="0 0 14 16" aria-hidden="true"><path fill="var(--blue)" d="M3 1 L6 4 L4.5 6 C5.5 8.5 7 10 9.5 11.5 L11.5 10 L14 13 L11.5 15.5 C5.5 14 1 9 0 3.5 Z"/></svg>
      <span>+8164-5290</span>
    </li>
    <li>
      <svg width="12" height="9" viewBox="0 0 12 9" aria-hidden="true"><rect width="12" height="9" rx="1" fill="var(--blue)"/><path d="M0.5 1 L6 5 L11.5 1" stroke="var(--ink-mid)" fill="none"/></svg>
      <span>daniel@tidemotion-sg.example</span>
    </li>
    <li>
      <svg width="12" height="12" viewBox="0 0 12 12" aria-hidden="true"><circle cx="6" cy="6" r="6" fill="var(--blue)"/><path d="M0 6 H12 M6 0 C3 3 3 9 6 12 M6 0 C9 3 9 9 6 12" stroke="var(--ink-mid)" fill="none" stroke-width="0.9"/></svg>
      <span>www.tidemotion-sg.example</span>
    </li>
  </ul>

  <p class="terms">* terms &amp; conditions apply</p>

  <p class="caption caption-kick">Kick Boxing Training</p>
  <p class="caption caption-pt">Personal Training</p>
</main>
</body>
</html>
```